Harbor Reel Works Needs A Web Layout Design
Aqua/Black/White used on the layout
Creative Brief
Entertainment
Harbor reel works is a company that deals with videography, photography, and dj services. It uses the colours of blue, black, and white. The logo that can be used can be either of the following : http://www.velmorafind.example/images/vendor/300/230/harbor-logo.jpg or http://img18.pixelnookhost.example/img18/2856/26226344958409311344955.jpg . You can put demo tabs for the menu for now because those are not committed upon, and the body should look professional for the niche that his business is.
I like the clean and professional look but i hate having a lack of creativity within the design . Also i want it to show that we are the best and that the person coming to our website HAS TO GO WITH US, based on a POP of our website to their eye.
High Tech
aqua blue

```html
<!DOCTYPE html>
<html lang="en">
<head>
<meta charset="utf-8">
<title>Harbor Reel Works</title>
<link rel="stylesheet" href="https://fonts.googleapis.com/css2?family=Open+Sans:wght@400;600;700;800&display=swap">
<style>
  :root{
    --aqua:#21c3d6;
    --aqua-light:#7fe6f2;
    --aqua-deep:#0f7f90;
    --teal-dark:#0a3640;
    --black:#030708;
    --panel:#0b1c22;
    --white:#ffffff;
    --muted:#bfd9de;
  }
  *{margin:0;padding:0;box-sizing:border-box}
  html,body{width:1200px;height:974px;overflow:hidden;background:var(--black)}
  body{font-family:"Open Sans",Arial,sans-serif;color:var(--white);position:relative}
  .page{position:absolute;inset:0;overflow:hidden;
    background:
      radial-gradient(ellipse 70% 30% at 50% 0%, #14606d 0%, #0a2a32 55%, transparent 80%),
      radial-gradient(ellipse 80% 25% at 50% 100%, #0d4650 0%, #062027 50%, transparent 80%),
      linear-gradient(#07191e, #020506 40%, #020506 75%, #06222a);}
  .header-arc{position:absolute;left:0;top:0;width:1200px;height:200px}
  .brand{position:absolute;left:50%;top:14px;transform:translateX(-50%);display:flex;align-items:center;gap:12px}
  .brand-mark{width:30px;height:30px;background:var(--aqua)}
  .brand-name{font-weight:800;font-size:26px;letter-spacing:3px;color:var(--aqua-light)}
  .nav{position:absolute;top:120px;left:205px;width:790px;display:flex;justify-content:space-between;align-items:center}
  .nav a{font-size:16px;font-weight:700;color:var(--aqua);text-decoration:none;letter-spacing:.5px}
  .nav a.active{color:var(--white)}
  .nav .sep{width:1px;height:22px;background:#2a5c66}
  .nav-line{position:absolute;top:156px;left:170px;width:860px;height:2px;background:linear-gradient(90deg,transparent,var(--aqua-deep),transparent)}
  .slider{position:absolute;left:205px;top:184px;width:790px;height:324px;border:3px solid var(--aqua);background:#000}
  .slider-photo{position:absolute;inset:6px;background:radial-gradient(circle at 30% 35%, #6b5a44 0%, #2a2118 30%, #080706 65%)}
  .slider-copy{position:absolute;left:425px;top:110px;width:340px}
  .slider-copy h2{font-size:27px;font-weight:700;margin-bottom:8px}
  .slider-copy p{font-size:15px;font-weight:700;line-height:21px}
  .arrow-tab{position:absolute;width:38px;height:64px;background:var(--aqua);display:flex;align-items:center;justify-content:center}
  .arrow-tab.left{left:-3px;top:110px;border-radius:0 32px 32px 0}
  .arrow-tab.right{right:-3px;top:110px;border-radius:32px 0 0 32px}
  .tabs{position:absolute;left:205px;top:534px;width:790px;height:40px;display:flex}
  .tab{flex:1;display:flex;align-items:center;justify-content:center;font-size:15px;font-weight:700;color:var(--aqua-deep);background:linear-gradient(#ffffff,#d8eef1);border-left:3px solid var(--aqua)}
  .tab.active{background:var(--aqua);color:var(--white);border-left:0}
  .releases{position:absolute;left:205px;top:574px;width:790px;height:224px;background:linear-gradient(#35c9da,#1790a2);border:3px solid #4fd5e4}
  .release-list{position:absolute;left:22px;top:20px;display:flex;gap:44px}
  .release{width:156px;text-align:center}
  .release-thumb{width:156px;height:128px;border:3px solid var(--white);margin-bottom:8px}
  .t1{background:linear-gradient(135deg,#f0c26a,#d8486a 60%,#7ab0d8)}
  .t2{background:linear-gradient(#6e6f6e,#3b3f44 60%,#2b2f35)}
  .t3{background:linear-gradient(135deg,#5c3a2c,#c97a5a 50%,#2a1a15)}
  .t4{background:linear-gradient(#72726f,#3e4246 60%,#2b2f35)}
  .release h3{font-size:11px;font-weight:700;color:var(--teal-dark)}
  .release a{font-size:10px;color:var(--white);text-decoration:none}
  .side-chevron{position:absolute;top:612px}
  .footer-line{position:absolute;top:850px;left:0;width:1200px;height:2px;background:linear-gradient(90deg,transparent,var(--aqua-deep),transparent)}
  .footer{position:absolute;top:870px;left:200px;width:800px;display:flex;font-size:13px;line-height:17px;color:var(--muted)}
  .footer-brand{width:140px;display:flex;align-items:center;gap:8px;font-weight:800;font-size:15px;color:var(--aqua-light);letter-spacing:1px;line-height:18px}
  .footer-brand .sq{width:16px;height:16px;background:var(--aqua);flex:none}
  .copy{width:205px;font-size:11px;line-height:15px}
  .copy a{color:var(--muted);text-decoration:none}
  .links{width:100px}
  .links a{display:block;color:var(--white);text-decoration:none}
  .social h4{font-size:13px;font-weight:400;color:var(--white);margin-bottom:6px}
  .social-icons{display:flex;gap:8px}
  .social-icons span{width:22px;height:22px;border-radius:3px}
</style>
</head>
<body>
<div class="page">
  <svg class="header-arc" viewBox="0 0 1200 200" aria-hidden="true">
    <path d="M0 95 Q600 210 1200 95" fill="none" stroke="#1c8c9c" stroke-width="2" opacity=".7"/>
    <path d="M0 60 Q600 160 1200 60" fill="none" stroke="#1c8c9c" stroke-width="1" opacity=".35"/>
  </svg>

  <div class="brand"><span class="brand-mark"></span><span class="brand-name">HARBOR REEL WORKS</span></div>

  <nav class="nav">
    <a class="active" href="#">HOME</a><span class="sep"></span>
    <a href="#">SERVICES</a><span class="sep"></span>
    <a href="#">VIDEOGRAPHY</a><span class="sep"></span>
    <a href="#">PHOTOGRAPHY</a><span class="sep"></span>
    <a href="#">DJ SERVICES</a><span class="sep"></span>
    <a href="#">CONTACT US</a>
  </nav>
  <div class="nav-line"></div>

  <section class="slider">
    <div class="slider-photo" role="img" aria-label="DJ performing at turntables under stage lights"></div>
    <div class="slider-copy">
      <h2>Neque porro quisquam</h2>
      <p>Lorem ipsum dolor sit amet, consectetur adipiscing elit. Nam hendrerit ligula at odio scelerisque vel lobortis magna</p>
    </div>
    <div class="arrow-tab left"><svg width="14" height="20" viewBox="0 0 14 20"><path d="M12 2 L3 10 L12 18" fill="none" stroke="#fff" stroke-width="4"/></svg></div>
    <div class="arrow-tab right"><svg width="14" height="20" viewBox="0 0 14 20"><path d="M2 2 L11 10 L2 18" fill="none" stroke="#fff" stroke-width="4"/></svg></div>
  </section>

  <div class="tabs">
    <div class="tab active">NEW RELEASES</div>
    <div class="tab">LATEST NEWS</div>
    <div class="tab">OUR SERVICES</div>
  </div>

  <section class="releases">
    <div class="release-list">
      <div class="release"><div class="release-thumb t1" role="img" aria-label="Colourful music release cover"></div><h3>LOREM IPSUM DOLOR</h3><a href="#">Know More &gt;&gt;</a></div>
      <div class="release"><div class="release-thumb t2" role="img" aria-label="Artist seated on a city street"></div><h3>LOREM IPSUM DOLOR</h3><a href="#">Know More &gt;&gt;</a></div>
      <div class="release"><div class="release-thumb t3" role="img" aria-label="Album cover with performer portrait"></div><h3>LOREM IPSUM DOLOR</h3><a href="#">Know More &gt;&gt;</a></div>
      <div class="release"><div class="release-thumb t4" role="img" aria-label="Artist seated on a city street"></div><h3>LOREM IPSUM DOLOR</h3><a href="#">Know More &gt;&gt;</a></div>
    </div>
  </section>
  <svg class="side-chevron" style="left:180px" width="34" height="100" viewBox="0 0 34 100" aria-hidden="true"><path d="M30 4 L6 50 L30 96" fill="none" stroke="#fff" stroke-width="8"/></svg>
  <svg class="side-chevron" style="left:986px" width="34" height="100" viewBox="0 0 34 100" aria-hidden="true"><path d="M4 4 L28 50 L4 96" fill="none" stroke="#fff" stroke-width="8"/></svg>

  <div class="footer-line"></div>
  <footer class="footer">
    <div class="footer-brand"><span class="sq"></span><span>HARBOR<br>REEL WORKS</span></div>
    <div class="copy">©2011 Harbor Reel Works.<br>All Rights Reserved.<br><a href="#">Terms of use</a> | <a href="#">Privacy Policy</a></div>
    <div class="links"><a href="#">Home</a><a href="#">Services</a><a href="#">News</a></div>
    <div class="links" style="width:120px"><a href="#">Videography</a><a href="#">Photography</a><a href="#">DJ Services</a></div>
    <div class="links" style="width:125px"><a href="#">New Releases</a><a href="#">Testimonials</a><a href="#">Contact Us</a></div>
    <div class="social"><h4>Social Networks</h4>
      <div class="social-icons"><span style="background:#3b5998"></span><span style="background:#c4302b"></span><span style="background:#4aa3df"></span></div>
    </div>
  </footer>
</div>
</body>
</html>
```